KORVAL Works Pty Ltd. Website and Domain

www.korvalworks.com.au

require email addresses setup.

Info@korvalworks.com.au
accounts@korvalworks.com.au
peter.gralow@korvalworks.com.au
lucas.brenner@korvalworks.com.au

Website should promote commercial and domestic electrical services, audio visual services and data and fibre installations.

similar to my mates site www.bryfield.com.au

Website needs to promote professionalism, electrical/electrician, audio visual and data/fibre cabling installations.

promote environmental friendly imaginary.

Coding

Coded - Design and coding required

```html
<!DOCTYPE html>
<html lang="en">
<head>
<meta charset="utf-8">
<title>KORVAL Works Pty Ltd. – Electrical, Audio Visual, Data</title>
<link href="https://fonts.googleapis.com/css2?family=Mulish:wght@300;400;600;700;800&family=Montserrat:wght@500;600;700&display=swap" rel="stylesheet">
<style>
:root{
  --green:#9cc93b;
  --blue:#2ea6df;
  --blue-card:#42b4e6;
  --ink:#2b2f36;
  --muted:#6a6f78;
  --light:#f3f6f9;
  --white:#ffffff;
}
*{margin:0;padding:0;box-sizing:border-box}
html,body{width:1200px;height:3990px;overflow:hidden}
body{font-family:"Mulish",sans-serif;color:var(--ink);background:var(--white);position:relative}
.abs{position:absolute}
.section-title{position:absolute;left:0;width:1200px;text-align:center;font-size:40px;font-weight:300;color:var(--green);letter-spacing:-.5px}
.section-title b{font-weight:800;color:var(--blue)}
.title-rule{position:absolute;left:572px;width:56px;height:3px;background:linear-gradient(90deg,var(--green),var(--blue))}

/* hero */
.hero{position:absolute;left:0;top:0;width:1200px;height:660px;overflow:hidden}
.hero-photo{position:absolute;inset:0;background:
  radial-gradient(ellipse at 25% 60%,rgba(196,120,70,.75),transparent 55%),
  radial-gradient(ellipse at 80% 35%,rgba(40,110,200,.7),transparent 55%),
  linear-gradient(180deg,#1a2333 0%,#3a3a44 45%,#4a4036 100%)}
.hero-shade{position:absolute;inset:0;background:rgba(0,0,0,.25)}
.call{left:118px;top:12px;color:var(--white);display:flex;align-items:center;gap:10px}
.call-text{font-size:14px;line-height:1.15}
.call-text strong{display:block;font-size:17px;font-weight:600}
.brand{display:flex;align-items:center;gap:10px}
.brand-mark{width:52px;height:52px;border-radius:50%;border:4px solid var(--green)}
.brand-name{font-family:"Montserrat",sans-serif;font-weight:700;font-size:30px;color:var(--blue);letter-spacing:.5px}
.hero .brand{left:478px;top:12px}
.socials{display:flex;gap:12px}
.social{width:26px;height:26px;border-radius:50%;border:2px solid rgba(255,255,255,.85)}
.hero .socials{left:972px;top:18px}
.nav{left:0;top:96px;width:1200px;display:flex;justify-content:center}
.nav a{color:var(--white);text-decoration:none;font-size:21px;padding:0 30px;border-right:1px dashed rgba(255,255,255,.35)}
.nav a:last-child{border-right:none}
.nav a.active{color:var(--green);text-decoration:underline;text-underline-offset:6px}
.hero-title{left:0;top:286px;width:1200px;text-align:center;color:var(--white);font-family:"Montserrat",sans-serif;font-weight:600;font-size:52px;line-height:66px}
.hero-sub{left:0;top:436px;width:1200px;text-align:center;color:var(--white);font-size:26px;font-weight:300}
.arrow-btn{width:42px;height:42px;border-radius:50%;display:flex;align-items:center;justify-content:center}
.arrow-prev{left:105px;top:287px;border:2px solid rgba(255,255,255,.7)}
.arrow-next{left:950px;top:287px;background:var(--blue)}

/* about */
.about{position:absolute;left:0;top:640px;width:1200px;height:523px;background:linear-gradient(180deg,#ffffff 0%,#eef1f4 100%)}
.about-art{left:125px;top:70px;width:410px;height:340px;border-radius:50%;background:radial-gradient(circle,rgba(46,166,223,.28) 0%,rgba(156,201,59,.22) 55%,transparent 72%)}
.about-title{left:582px;top:78px;font-size:40px;font-weight:400;color:var(--green)}
.about-title b{font-weight:400;color:var(--blue)}
.about p{position:absolute;left:582px;width:440px}
.p-small{font-size:14px;line-height:27px;color:var(--muted)}
.p-lead{font-size:17px;line-height:28px;color:var(--ink)}

/* why */
.why-card{position:absolute;top:1353px;width:351px;height:354px;text-align:center}
.why-card.featured{background:var(--blue-card);color:var(--white);box-shadow:0 10px 30px rgba(46,166,223,.25)}
.why-icon{position:absolute;left:135px;top:60px}
.why-card h3{position:absolute;left:0;top:192px;width:100%;font-size:15px;font-weight:600;line-height:26px}
.why-card p{position:absolute;left:50px;top:258px;width:251px;font-size:14px;line-height:24px;color:var(--muted)}
.why-card.featured p,.why-card.featured h3{color:var(--white)}

/* services dark */
.services{position:absolute;left:0;top:1830px;width:1200px;height:730px;overflow:hidden}
.services-photo{position:absolute;inset:0;background:
  radial-gradient(ellipse at 70% 30%,rgba(214,126,60,.7),transparent 50%),
  radial-gradient(ellipse at 20% 70%,rgba(60,80,110,.6),transparent 55%),
  linear-gradient(180deg,#1e2a3c 0%,#303c4e 50%,#1d2430 100%)}
.services-shade{position:absolute;inset:0;background:rgba(10,18,30,.45)}
.services .section-title{top:76px}
.services-art{left:447px;top:200px;width:393px;height:330px;border-radius:50%;background:radial-gradient(circle,rgba(46,166,223,.35) 0%,rgba(156,201,59,.25) 55%,transparent 72%)}
.svc{position:absolute;color:var(--white)}
.svc h4{font-family:"Montserrat",sans-serif;font-weight:600;font-size:21px;line-height:23px;margin-bottom:12px}
.svc p{font-size:15px;line-height:24px;color:rgba(255,255,255,.85);width:190px}
.svc-icon{position:absolute;width:84px;height:84px;border-radius:50%;background:var(--white);display:flex;align-items:center;justify-content:center;box-shadow:0 0 0 5px rgba(46,166,223,.25)}
.learn{left:521px;top:567px;width:165px;height:46px;background:var(--blue);color:var(--white);font-size:17px;display:flex;align-items:center;justify-content:center;gap:8px;border-radius:2px}

/* testimonials */
.review{position:absolute;top:2715px;width:275px;height:263px;background:var(--white);border:1px solid #e4e7eb;padding:26px 30px}
.review.raised{box-shadow:0 8px 26px rgba(0,0,0,.08);border-color:#eef0f2}
.stars{color:#f4a11a;font-size:18px;letter-spacing:2px}
.review h5{font-size:13px;font-weight:700;margin:8px 0 10px}
.review p{font-size:12px;line-height:20px;color:var(--muted)}
.author{position:absolute;left:30px;top:196px;display:flex;align-items:center;gap:12px}
.avatar{width:30px;height:30px;border-radius:50%;background:linear-gradient(135deg,#9aa3ad,#4b525a)}
.author strong{display:block;font-size:12px;font-weight:700}
.author span{font-size:12px;color:var(--muted)}
.dots{left:565px;top:3016px;display:flex;gap:8px}
.dot{width:11px;height:11px;border-radius:50%;border:1px solid #9aa3ad}
.dot.on{background:var(--blue);border-color:var(--blue)}

/* contact */
.contact-band{position:absolute;left:0;top:3192px;width:1200px;height:400px;overflow:hidden}
.contact-photo{position:absolute;inset:0;background:radial-gradient(ellipse at 75% 40%,rgba(180,90,70,.55),transparent 55%),linear-gradient(90deg,#2a313c,#3b3f48)}
.contact-shade{position:absolute;inset:0;background:rgba(10,16,24,.45)}
.form-card{position:absolute;left:119px;top:3150px;width:506px;height:487px;border-radius:110px 0 110px 0;background:linear-gradient(160deg,#2aa3de 0%,#4bb1c6 50%,#a7d23a 100%)}
.field{position:absolute;background:rgba(255,255,255,.88);border:1px solid rgba(255,255,255,.95);font-size:13px;color:#7b828c;padding:7px 12px}
.send{position:absolute;left:397px;top:3485px;width:144px;height:35px;border:2px solid var(--white);color:var(--white);font-size:16px;display:flex;align-items:center;justify-content:center}
.contact-info{left:724px;top:3268px;color:var(--white)}
.contact-info h2{font-family:"Montserrat",sans-serif;font-weight:500;font-size:31px;margin-bottom:26px}
.info-row{display:flex;gap:16px;align-items:flex-start;font-size:16px;line-height:27px;margin-bottom:16px}
.info-row svg{flex:none;margin-top:5px}

/* footer */
.footer{position:absolute;left:0;top:3592px;width:1200px;height:398px;background:var(--light)}
.footer .brand{left:478px;top:128px}
.footer-nav{left:0;top:224px;width:1200px;display:flex;justify-content:center;gap:38px;font-size:16px;color:var(--ink)}
.footer .socials{left:542px;top:276px;gap:20px}
.footer .social{width:22px;height:22px;border-color:var(--blue)}
.footer-rule{left:0;top:333px;width:1200px;height:1px;background:#d9dde2}
.copyright{left:120px;top:352px;font-size:14px;color:var(--muted)}
.legal{right:138px;top:352px;font-size:14px;color:var(--muted)}
</style>
</head>
<body>

<!-- Hero -->
<header class="hero">
  <div class="hero-photo" role="img" aria-label="Photo of an electrician working on a wired switchboard"></div>
  <div class="hero-shade"></div>

  <div class="abs call">
    <svg width="40" height="40" viewBox="0 0 40 40" fill="none" stroke="#fff" stroke-width="2"><circle cx="20" cy="20" r="17"/><path d="M14 12l4 4-2 3c1 2 3 4 5 5l3-2 4 4-2 3c-7 0-14-7-14-14z"/></svg>
    <div class="call-text">Call Us<strong>02 5550 1427</strong></div>
  </div>

  <div class="abs brand">
    <span class="brand-mark"></span><span class="brand-name">KORVAL Works</span>
  </div>

  <div class="abs socials" aria-label="Social links">
    <span class="social"></span><span class="social"></span><span class="social"></span>
  </div>

  <nav class="abs nav">
    <a class="active">Home</a><a>About us</a><a>Services</a><a>Gallery</a><a>Contact</a>
  </nav>

  <div class="abs arrow-btn arrow-prev"><svg width="14" height="20" viewBox="0 0 14 20" fill="none" stroke="#fff" stroke-width="2"><path d="M11 2L3 10l8 8"/></svg></div>
  <div class="abs arrow-btn arrow-next"><svg width="14" height="20" viewBox="0 0 14 20" fill="none" stroke="#fff" stroke-width="2.5"><path d="M3 2l8 8-8 8"/></svg></div>

  <h1 class="abs hero-title">See What We Can<br>Do For You</h1>
  <p class="abs hero-sub">Electrical . Audio Visual . Data</p>
  <svg class="abs" style="left:580px;top:510px" width="40" height="18" viewBox="0 0 40 18" fill="none" stroke="#fff" stroke-width="2"><path d="M2 3l18 12L38 3"/></svg>

  <svg class="abs" style="left:0;top:560px" width="1200" height="100" viewBox="0 0 1200 100">
    <defs><linearGradient id="heroCurve" x1="0" x2="1"><stop offset="0" stop-color="#9cc93b"/><stop offset="1" stop-color="#2ea6df"/></linearGradient></defs>
    <path d="M0 100 L0 90 C300 20 850 5 1200 100 Z" fill="#fff"/>
    <path d="M120 90 C380 10 800 0 1080 86" fill="none" stroke="url(#heroCurve)" stroke-width="6"/>
  </svg>
</header>

<!-- About -->
<section class="about">
  <div class="abs about-art" role="img" aria-label="Large decorative brand emblem"></div>
  <h2 class="abs about-title">About <b>KORVAL Works</b></h2>
  <p class="p-small" style="top:152px">Lorem Ipsum is simply dummy text of the printing and typesetting industry. Lorem Ipsum has been the industry's standard</p>
  <p class="p-lead" style="top:224px">Lorem Ipsum is simply dummy text of the printing and typesetting industry.</p>
  <p class="p-small" style="top:295px">Lorem Ipsum is simply dummy text of the printing and typesetting industry. Lorem Ipsum has been the industry's standard dummy text ever since the 1500s, when an unknown printer took a galley of type and scrambled it to make a type specimen book.</p>
</section>

<!-- Why choose us -->
<h2 class="section-title" style="top:1240px">Why <b>Choose Us</b></h2>
<div class="title-rule" style="top:1299px"></div>

<div class="why-card" style="left:86px">
  <svg class="why-icon" width="80" height="80" viewBox="0 0 80 80" fill="none" stroke-width="3">
    <circle cx="40" cy="40" r="36" stroke="#2ea6df"/>
    <path d="M25 41l10 10 20-22" stroke="#555" stroke-linecap="round" stroke-linejoin="round"/>
  </svg>
  <h3>Professional<br>Standards</h3>
  <p>Lorem Ipsum is simply dummy text of the printing and typesetting</p>
</div>

<div class="why-card featured" style="left:421px">
  <svg class="why-icon" width="80" height="80" viewBox="0 0 80 80" fill="none" stroke="#fff" stroke-width="3">
    <circle cx="40" cy="40" r="36"/>
    <rect x="26" y="28" width="28" height="24" stroke-width="2.5"/><path d="M26 40h28M40 28v24" stroke-width="2"/>
  </svg>
  <h3>Quality Workmanship<br>Guaranteed</h3>
  <p>Lorem Ipsum is simply dummy text of the printing and typesetting</p>
</div>

<div class="why-card" style="left:778px">
  <svg class="why-icon" width="80" height="80" viewBox="0 0 80 80" fill="none" stroke-width="3">
    <circle cx="40" cy="40" r="36" stroke="#2ea6df"/>
    <rect x="27" y="24" width="26" height="32" rx="2" stroke="#555" stroke-width="2.5"/>
    <path d="M32 34h16M32 41h16M32 48h10" stroke="#555" stroke-width="2"/>
  </svg>
  <h3>Complete Package For Business<br>And Sustainable Practices</h3>
  <p>Lorem Ipsum is simply dummy text of the printing and typesetting</p>
</div>

<!-- Services -->
<section class="services">
  <div class="services-photo" role="img" aria-label="Photo of a suburban street at dusk"></div>
  <div class="services-shade"></div>
  <h2 class="section-title">Our <b style="color:var(--green)">Services</b></h2>
  <div class="title-rule" style="top:132px"></div>

  <div class="abs services-art" role="img" aria-label="Large decorative brand emblem"></div>

  <div class="svc" style="left:152px;top:190px"><h4>Electrical Services</h4><p>Lorem Ipsum is simply dummy text of the printing and typesetting industry.</p></div>
  <div class="svc-icon" style="left:370px;top:203px"><svg width="44" height="44" viewBox="0 0 44 44" fill="none" stroke="#333" stroke-width="2"><circle cx="22" cy="22" r="15"/><path d="M24 10l-8 14h7l-3 10 9-15h-7z"/></svg></div>

  <div class="svc" style="left:834px;top:155px"><h4>Data Services</h4><p>Lorem Ipsum is simply dummy text of the printing and typesetting industry.</p></div>
  <div class="svc-icon" style="left:723px;top:170px"><svg width="44" height="44" viewBox="0 0 44 44" fill="none" stroke="#333" stroke-width="2"><rect x="8" y="10" width="28" height="18" rx="2"/><path d="M22 28v6M14 36h16"/></svg></div>

  <div class="svc" style="left:873px;top:364px"><h4>Fibre Cabling<br>Installations</h4><p>Lorem Ipsum is simply dummy text of the printing and typesetting industry.</p></div>
  <div class="svc-icon" style="left:765px;top:383px"><svg width="44" height="44" viewBox="0 0 44 44" fill="none" stroke="#333" stroke-width="2"><circle cx="22" cy="22" r="17"/><circle cx="22" cy="22" r="12"/><circle cx="22" cy="22" r="7"/><circle cx="22" cy="22" r="2"/></svg></div>

  <div class="svc" style="left:177px;top:430px"><h4>Audio Visual<br>Services</h4><p>Lorem Ipsum is simply dummy text of the printing and typesetting industry.</p></div>
  <div class="svc-icon" style="left:384px;top:448px"><svg width="44" height="44" viewBox="0 0 44 44" stroke="#333" stroke-width="3" stroke-linecap="round"><path d="M8 18v8M14 12v20M20 6v32M26 10v24M32 15v14M38 19v6"/></svg></div>

  <div class="abs learn">Learn More <svg width="22" height="12" viewBox="0 0 22 12" fill="none" stroke="#fff" stroke-width="2"><path d="M0 6h20M15 1l5 5-5 5"/></svg></div>

  <svg class="abs" style="left:0;top:650px" width="1200" height="80" viewBox="0 0 1200 80">
    <path d="M0 80 L0 42 C380 -2 820 -2 1200 42 L1200 80 Z" fill="#fff"/>
    <path d="M0 40 C380 -4 820 -4 1200 40" fill="none" stroke="#9cc93b" stroke-width="5"/>
  </svg>
</section>

<!-- Testimonials -->
<h2 class="section-title" style="top:2622px">Our <b style="color:var(--green)">Services</b></h2>
<div class="title-rule" style="top:2681px"></div>

<article class="review" style="left:168px">
  <div class="stars">★★★★★</div>
  <h5>“SOLID Service! Vety consistent!”</h5>
  <p>the printing and typesetting industry. Lorem Ipsum has been the industry's standard dummy text ever since the 1500s Lorem Ipsum!</p>
  <div class="author"><span class="avatar" role="img" aria-label="Client portrait"></span><div><strong>Marla Quint</strong><span>Web Development</span></div></div>
</article>
<article class="review raised" style="left:464px">
  <div class="stars">★★★★★</div>
  <h5>“SOLID Service! Vety consistent!”</h5>
  <p>the printing and typesetting industry. Lorem Ipsum has been the industry's standard dummy text ever since the 1500s Lorem Ipsum!</p>
  <div class="author"><span class="avatar" role="img" aria-label="Client portrait"></span><div><strong>Marla Quint</strong><span>Web Development</span></div></div>
</article>
<article class="review" style="left:758px">
  <div class="stars">★★★★★</div>
  <h5>“SOLID Service! Vety consistent!”</h5>
  <p>the printing and typesetting industry. Lorem Ipsum has been the industry's standard dummy text ever since the 1500s Lorem Ipsum!</p>
  <div class="author"><span class="avatar" role="img" aria-label="Client portrait"></span><div><strong>Marla Quint</strong><span>Web Development</span></div></div>
</article>
<div class="abs dots"><span class="dot"></span><span class="dot on"></span><span class="dot"></span><span class="dot"></span></div>

<!-- Contact -->
<section class="contact-band">
  <div class="contact-photo" role="img" aria-label="Photo of a technician testing wiring"></div>
  <div class="contact-shade"></div>
</section>
<div class="form-card"></div>
<div class="field" style="left:205px;top:3265px;width:164px;height:33px">Name</div>
<div class="field" style="left:378px;top:3265px;width:163px;height:33px;text-align:center">Email</div>
<div class="field" style="left:205px;top:3310px;width:336px;height:33px">Subject</div>
<div class="field" style="left:205px;top:3355px;width:336px;height:117px">Message</div>
<div class="send">Send</div>

<div class="abs contact-info">
  <h2>Get In Touch With Us</h2>
  <div class="info-row"><svg width="20" height="22" viewBox="0 0 20 22" fill="none" stroke="#fff" stroke-width="1.8"><path d="M10 21s7-7 7-12a7 7 0 0 0-14 0c0 5 7 12 7 12z"/><circle cx="10" cy="9" r="2.5"/></svg><span>48 Ferncourt Lane, Unit 6<br>Marrinvale NSW 2760</span></div>
  <div class="info-row"><svg width="20" height="20" viewBox="0 0 20 20" fill="#fff"><path d="M4 1l4 4-2 3c1 2 4 5 6 6l3-2 4 4-3 3C8 19 1 12 1 4z"/></svg><span>(02) 5550 1427</span></div>
  <div class="info-row"><svg width="20" height="16" viewBox="0 0 20 16" fill="none" stroke="#fff" stroke-width="1.8"><rect x="1" y="1" width="18" height="14"/><path d="M1 1l9 8 9-8"/></svg><span>Info@korvalworks.com.au</span></div>
</div>

<!-- Footer -->
<footer class="footer">
  <div class="abs brand"><span class="brand-mark"></span><span class="brand-name">KORVAL Works</span></div>
  <nav class="abs footer-nav"><span>Home</span><span>About Us</span><span>Services</span><span>Gallery</span><span>Contact</span></nav>
  <div class="abs socials" aria-label="Social links"><span class="social"></span><span class="social"></span><span class="social"></span></div>
  <div class="abs footer-rule"></div>
  <p class="abs copyright">Copyright 2020 KORVAL Works Pty Ltd. All Rights Reserved.</p>
  <p class="abs legal">Privacy Policy &nbsp; | &nbsp; Terms Of Services</p>
</footer>

</body>
</html>
```